Business Cards

I'd like help creating business cards with the full logo "Veltrona Capital Partners" on the back of the card (navy background with white writing), and abbreviated logo "VCP" on the front. Would like to list name, title, phone number, email, and website listed on front of card. Would like to keep very simple. Front font Arial or similar.

```html
<!DOCTYPE html>
<html lang="en">
<head>
<meta charset="utf-8">
<title>Veltrona Capital Partners – Business Cards</title>
<link href="https://fonts.googleapis.com/css2?family=Archivo:wght@700;800&family=Montserrat:wght@500;600&display=swap" rel="stylesheet">
<style>
  :root {
    --stage: #322f30;
    --paper: #ffffff;
    --ink: #111111;
    --navy: #1f3869;
    --navy-deep: #1c3362;
    --white: #ffffff;
  }
  * { margin: 0; padding: 0; box-sizing: border-box; }
  html, body { width: 1200px; height: 800px; overflow: hidden; background: var(--stage); }
  .canvas { position: relative; width: 1200px; height: 800px; }

  .card { position: absolute; overflow: hidden; }

  /* Front */
  .card-front { left: 364px; top: 56px; width: 430px; height: 245px; background: var(--paper); }
  .front-top { position: absolute; left: 0; top: 0; width: 100%; height: 153px; }
  .brand-short {
    position: absolute; left: 12px; top: 40px;
    font-family: "Archivo", Arial, sans-serif; font-weight: 800;
    font-size: 74px; line-height: 1; color: var(--ink); letter-spacing: 1px;
  }
  .person { position: absolute; right: 14px; top: 25px; text-align: right; color: var(--ink); font-family: "Archivo", Arial, sans-serif; }
  .person-name { font-weight: 800; font-size: 19.5px; letter-spacing: 0.5px; line-height: 1; }
  .person-title { font-weight: 700; font-size: 14.5px; margin-top: 3px; line-height: 1; }
  .rule { position: absolute; left: 0; top: 153px; width: 100%; height: 7px; background: var(--ink); }
  .front-bottom { position: absolute; left: 0; top: 160px; width: 100%; height: 85px; background: var(--navy); }
  .contacts { position: absolute; left: 17px; top: 36px; display: flex; align-items: center; }
  .contact { display: flex; align-items: center; margin-right: 14px; font-family: "Montserrat", Arial, sans-serif; font-weight: 600; font-size: 9.6px; color: var(--white); white-space: nowrap; }
  .contact:last-child { margin-right: 0; }
  .contact-icon { width: 20px; height: 20px; margin-right: 7px; flex: none; }

  /* Back */
  .card-back { left: 365px; top: 405px; width: 427px; height: 253px; background: var(--navy); }
  .back-mark {
    position: absolute; left: 0; top: 0; width: 100%; height: 100%;
    display: flex; align-items: center; justify-content: center;
    font-family: "Archivo", Arial, sans-serif; font-weight: 800;
    font-size: 190px; color: var(--navy-deep); letter-spacing: 4px; line-height: 1;
  }
  .wordmark { position: absolute; left: 0; top: 86px; width: 100%; text-align: center; color: var(--white); font-family: "Montserrat", Arial, sans-serif; font-weight: 600; }
  .wordmark-name { font-size: 41px; line-height: 1; letter-spacing: 1px; }
  .wordmark-sub { font-size: 13.5px; line-height: 1; letter-spacing: 7.2px; margin-top: 12px; margin-right: -7px; }
</style>
</head>
<body>
<main class="canvas">

  <section class="card card-front" aria-label="Business card front">
    <div class="front-top">
      <div class="brand-short">VCP</div>
      <div class="person">
        <p class="person-name">MAREK DVORSKY</p>
        <p class="person-title">CEO</p>
      </div>
    </div>
    <div class="rule"></div>
    <div class="front-bottom">
      <div class="contacts">
        <p class="contact">
          <svg class="contact-icon" viewBox="0 0 20 20" aria-hidden="true">
            <circle cx="10" cy="10" r="10" fill="#111"/>
            <path d="M6.6 5.2l1.6-.4 1.1 2.4-1 .9c.5 1.2 1.4 2.1 2.6 2.7l.9-1 2.4 1.1-.4 1.6c-.2.5-.7.8-1.2.7-3.3-.5-5.9-3.1-6.4-6.4-.1-.5.2-1 .4-1.6z" fill="#fff"/>
          </svg>
          +420 602 318 745
        </p>
        <p class="contact">
          <svg class="contact-icon" viewBox="0 0 20 20" aria-hidden="true">
            <circle cx="10" cy="10" r="10" fill="#111"/>
            <g fill="none" stroke="#fff" stroke-width="1.1">
              <circle cx="10" cy="10" r="5"/>
              <ellipse cx="10" cy="10" rx="2.2" ry="5"/>
              <line x1="5" y1="10" x2="15" y2="10"/>
              <line x1="5.7" y1="7.5" x2="14.3" y2="7.5"/>
              <line x1="5.7" y1="12.5" x2="14.3" y2="12.5"/>
            </g>
          </svg>
          www.veltronacap.com
        </p>
        <p class="contact">
          <svg class="contact-icon" viewBox="0 0 20 20" aria-hidden="true">
            <circle cx="10" cy="10" r="10" fill="#111"/>
            <rect x="5.5" y="7" width="9" height="6.4" rx="0.8" fill="#fff"/>
            <path d="M5.8 7.4L10 10.6l4.2-3.2" fill="none" stroke="#111" stroke-width="1"/>
          </svg>
          hello@veltrona.com
        </p>
      </div>
    </div>
  </section>

  <section class="card card-back" aria-label="Business card back">
    <div class="back-mark" aria-hidden="true">VCP</div>
    <div class="wordmark">
      <p class="wordmark-name">VELTRONA</p>
      <p class="wordmark-sub">CAPITAL PARTNERS</p>
    </div>
  </section>

</main>
</body>
</html>
```